Letterhead Design for Higher Education provider

Company Name: PELV Credentials
Motto: Quality in Learning
Address: Tamble House, Orchard Rise, Fenwick Trade Park, Dartford DA4 9LX, United Kingdom
T: +44 (0)20 7946 0382
E: info@pelv-example.org.uk
W: www.pelv-example.org.uk
Legal information: PELV Credentials is incorporated in England & Wales | Company Reg. No. 07315248

Target Market(s)

Higher Education provider

Industry/Entity Type

Education

Font styles to use
Sans Serif

Requirements
Must have
• Company Name, Address, tel, email, web, company legal information.
Nice to have
• motto
Should not have
• should not cover to much of printing areas

```html
<!DOCTYPE html>
<html lang="en">
<head>
<meta charset="utf-8">
<title>PELV Credentials Letterhead</title>
<link href="https://fonts.googleapis.com/css2?family=Didact+Gothic&display=swap" rel="stylesheet">
<style>
  :root {
    --brand-blue: #0c34c4;
    --paper: #ffffff;
    --ink: #1a1a1a;
  }
  html, body {
    margin: 0;
    padding: 0;
    overflow: hidden;
  }
  body {
    width: 927px;
    height: 1200px;
    font-family: "Didact Gothic", "Century Gothic", sans-serif;
  }
  .letterhead {
    position: relative;
    width: 927px;
    height: 1200px;
    background: var(--brand-blue);
    overflow: hidden;
  }
  .sheet {
    position: absolute;
    left: 57px;
    top: 40px;
    width: 813px;
    height: 1118px;
    background: var(--paper);
    border-radius: 38px;
  }
  .masthead {
    position: absolute;
    top: 22px;
    left: 0;
    width: 100%;
    text-align: center;
  }
  .brand-name {
    margin: 0;
    color: var(--brand-blue);
    font-size: 54px;
    font-weight: 400;
    line-height: 64px;
  }
  .reg-no {
    margin: 34px 0 0;
    color: var(--brand-blue);
    font-size: 10px;
    line-height: 12px;
  }
  .contact-footer {
    position: absolute;
    bottom: 6px;
    left: 0;
    width: 100%;
    text-align: center;
    color: var(--ink);
    font-size: 16.5px;
    line-height: 20px;
    white-space: nowrap;
  }
  .contact-footer p { margin: 0; }
  .contact-item {
    display: inline-flex;
    align-items: center;
    gap: 3px;
    margin: 0 2px;
  }
  .contact-icon {
    width: 10px;
    height: 10px;
    fill: var(--brand-blue);
  }
</style>
</head>
<body>
<div class="letterhead">
  <div class="sheet">
    <header class="masthead">
      <h1 class="brand-name">PELV Credentials</h1>
      <p class="reg-no">Reg. No. 07315248</p>
    </header>

    <footer class="contact-footer">
      <p>Tamble House, Orchard Rise, Fenwick Trade Park, Dartford DA4 9LX, United Kingdom</p>
      <p>
        <span class="contact-item">
          <svg class="contact-icon" viewBox="0 0 10 10" aria-hidden="true"><path d="M1 3.5C1 2 2 1.5 5 1.5S9 2 9 3.5L7.5 4.3 7 3.2H3L2.5 4.3Z"/><rect x="2.2" y="4.5" width="5.6" height="4" rx="0.6"/></svg>
          +44 (0)20 7946 0382
        </span>
        <span class="contact-item">
          <svg class="contact-icon" viewBox="0 0 10 10" aria-hidden="true"><path d="M0.5 2h9v6h-9z M1.3 2.6 5 5.4 8.7 2.6" stroke="#fff" stroke-width="0.7"/></svg>
          info@pelv-example.org.uk
        </span>
        <span class="contact-item">
          <svg class="contact-icon" viewBox="0 0 10 10" aria-hidden="true"><circle cx="5" cy="5" r="4.5"/><path d="M0.5 5h9M5 0.5v9M1.5 3h7M1.5 7h7" stroke="#fff" stroke-width="0.5" fill="none"/></svg>
          www.pelv-example.org.uk
        </span>
      </p>
    </footer>
  </div>
</div>
</body>
</html>
```